Larkmoor Health- Core Values Graphic for Visual Appeal

I would like a poster that could take these written core values from our organization and create a graphic that we could use for our staff and employees. I would also like to incorporate our branding into this project. Thank you!

Target Market(s)

To helps patients and employees understand the core values of our organization

Industry/Entity Type

Healthcare

Requirements
Must have
• Match our branding
Nice to have
• Please use your creativity!
Should not have
• Overly complex/ busy

```html
<!DOCTYPE html>
<html lang="en">
<head>
<meta charset="utf-8">
<title>Larkmoor Health – Core Values</title>
<link rel="stylesheet" href="https://fonts.googleapis.com/css2?family=Archivo+Black&family=Ubuntu:wght@400;500&display=swap">
<style>
  :root {
    --ink: #2b2b2d;
    --brand-blue: #2592d0;
    --bright-blue: #2aa3df;
    --paper: #f4f5f6;
    --paper-blue: #d3e8f3;
    --line: #b9c6cf;
    --line-blue: #9fcbe6;
    --white: #ffffff;
  }
  * { margin: 0; padding: 0; box-sizing: border-box; }
  html, body { width: 925px; height: 1200px; overflow: hidden; background: var(--paper); }
  .poster {
    position: relative;
    width: 925px;
    height: 1200px;
    overflow: hidden;
    background: linear-gradient(100deg, var(--paper-blue) 0%, #e9f1f6 35%, var(--paper) 60%, #eef4f8 100%);
    font-family: "Ubuntu", sans-serif;
  }
  .poster-title {
    position: absolute;
    right: 43px;
    top: 44px;
    text-align: right;
    font-family: "Archivo Black", sans-serif;
    font-size: 70px;
    line-height: 0.93;
    letter-spacing: 5px;
    color: var(--ink);
  }
  .values-panel {
    position: absolute;
    left: 609px;
    top: 226px;
    width: 316px;
    height: 659px;
    background: var(--brand-blue);
  }
  .value-text {
    position: absolute;
    left: 35px;
    width: 243px;
    color: var(--white);
    font-size: 11.8px;
    line-height: 14px;
    text-align: justify;
  }
  .artwork { position: absolute; inset: 0; }
  .value-word { font-family: "Archivo Black", sans-serif; font-size: 132px; }
  .value-word--blue { fill: var(--bright-blue); }
  .value-word--dark { fill: var(--ink); }
  .icon-slot { position: absolute; border-radius: 12px; background: radial-gradient(circle, rgba(42,163,223,0.25), rgba(43,43,45,0.08)); }
  .website-tab {
    position: absolute;
    left: 0;
    top: 917px;
    width: 53px;
    height: 283px;
    background: var(--ink);
    border-top-right-radius: 22px;
  }
  .website-tab span {
    position: absolute;
    left: 50%;
    top: 50%;
    transform: translate(-50%, -50%) rotate(-90deg);
    white-space: nowrap;
    color: var(--white);
    font-size: 14px;
    font-weight: 500;
    letter-spacing: 0.3px;
  }
  .brand-mark {
    position: absolute;
    left: 640px;
    top: 1048px;
    width: 250px;
    display: flex;
    align-items: center;
    gap: 10px;
    font-weight: 500;
    font-size: 26px;
    color: var(--ink);
  }
  .brand-mark .brand-dot { width: 20px; height: 20px; border-radius: 50%; background: var(--bright-blue); flex: none; }
</style>
</head>
<body>
<main class="poster">
  <svg class="artwork" width="925" height="1200" viewBox="0 0 925 1200" aria-hidden="true">
    <g fill="none" stroke-width="3" stroke-linecap="round" stroke-linejoin="round">
      <path d="M105 277 V108 Q105 92 121 92 H429 Q445 92 445 108 V244 Q445 258 459 258 H609" stroke="var(--line-blue)"/>
      <path d="M282 175 H488 Q502 175 502 189 V394 Q502 408 516 408 H609" stroke="var(--line)"/>
      <path d="M444 935 V457 Q444 443 458 443 H570 Q584 443 584 457 V564 Q584 578 598 578 H609" stroke="var(--line-blue)"/>
      <path d="M580 1106 V743 Q580 729 594 729 H609" stroke="var(--line)"/>
    </g>
    <g>
      <circle cx="609" cy="258" r="7" fill="var(--bright-blue)" stroke="var(--white)" stroke-width="2"/>
      <circle cx="609" cy="408" r="7" fill="var(--ink)" stroke="var(--white)" stroke-width="2"/>
      <circle cx="609" cy="578" r="7" fill="var(--bright-blue)" stroke="var(--white)" stroke-width="2"/>
      <circle cx="609" cy="729" r="7" fill="var(--ink)" stroke="var(--white)" stroke-width="2"/>
    </g>
    <text class="value-word value-word--blue" transform="translate(153 757) rotate(-90)" textLength="479" lengthAdjust="spacingAndGlyphs">FAMILY</text>
    <text class="value-word value-word--dark" transform="translate(280 1016) rotate(-90)" textLength="870" lengthAdjust="spacingAndGlyphs">EXCELLENCE</text>
    <text class="value-word value-word--blue" transform="translate(420 963) rotate(-90)" textLength="690" lengthAdjust="spacingAndGlyphs">INTIGRITY</text>
    <text class="value-word value-word--dark" transform="translate(565 1137) rotate(-90)" textLength="577" lengthAdjust="spacingAndGlyphs">SERVICE</text>
  </svg>

  <h1 class="poster-title">CORE<br>VALUES</h1>

  <section class="values-panel">
    <p class="value-text" style="top:27px">Family: At the heart of our mission is the commitment to provide high-quality, affordable healthcare in a comforting and uplifting family-oriented environment. Just as our community is our extended family, every patient is cherished member of our healthcare family. We treat each individual with the same care, compassion, and respect we would offer to our own loved ones.</p>
    <p class="value-text" style="top:181px">Excellence: In line with our goal, we aspire not only to alleviate pain but also to inspire patients to become active participants in their well-being. We believe in empowering our patients through education and compassion. Our pursuit of excellence is unwavering, driven by our dedication to continuously improve our services at every level, ensuring that our community receives nothing less than exceptional care.</p>
    <p class="value-text" style="top:351px">Integrity: In our healthcare team, 'Integrity' is non-negotiable. Our purpose is deeply rooted in ethics, integrity, and professional standards. We operate with the utmost integrity in every aspect of our work, adhering to the highest ethical principles. We understand that trust is the foundation of healthcare, and we are committed to maintaining the trust our community places in us.</p>
    <p class="value-text" style="top:502px">Service: Our vision is grounded in the belief that every person possesses the innate potential for true health. We aim to facilitate the body's natural healing response by providing the highest level of service. Our hope for each patient extends beyond healing; we aspire to help you fulfill your life's mission and purpose abundantly, supporting you in your journey to well-being.</p>
  </section>

  <div class="icon-slot" role="img" aria-label="Outline icon of a family group" style="left:43px;top:788px;width:121px;height:94px"></div>
  <div class="icon-slot" role="img" aria-label="Award rosette icon with a dollar sign" style="left:194px;top:1039px;width:92px;height:103px"></div>
  <div class="icon-slot" role="img" aria-label="Handshake icon beneath a shield with a tick" style="left:328px;top:989px;width:101px;height:90px"></div>
  <div class="icon-slot" role="img" aria-label="Open hands holding a gear icon" style="left:463px;top:443px;width:101px;height:103px"></div>

  <div class="website-tab"><span>WWW.LARKMOORHEALTH.COM</span></div>

  <div class="brand-mark"><span class="brand-dot"></span>Larkmoor Health</div>
</main>
</body>
</html>
```